RP Consult - Web Design Upgrade

We have recently designed a website (http://www.rpconsult-demo.com.au) which requires more creative and professional inputs. The website was designed using 'velvet harbour site builder template' and it is currently available for viewing on the internet. Also, you are able to access the PDF files for the 6 main pages (i.e. Home, About, Services, Contaminated Land Management, Groundwater Management and Contact).

The current website has 17 pages, however, your design may only be required for the 6 main pages.

Currently the website background is white but we are open to other colours provided the company logo is adjusted accordingly.

The idea is to upgrade the existing design and, if possible, continue using 'velvet harbour' as the preferred web host. So we are not sure if the design should be coded or uncoded...we leave it to your proficiency and advice.

Target Market(s)

Government organisations, landowners and developers, waste and utilities companies, community organisations and individuals.

Industry/Entity Type

Internet

Number of Pages Required

5+ page

Font styles to use
Sans Serif

Colors
0355a3
3176b5
9ccb3b
acd037
ffffff

Requirements
Nice to have
• Sliding images

```html
<!DOCTYPE html>
<html lang="en">
<head>
<meta charset="utf-8">
<title>RP Consult – Home</title>
<link href="https://fonts.googleapis.com/css2?family=Arimo:ital,wght@0,400;0,700;1,400&display=swap" rel="stylesheet">
<style>
  :root {
    --brand-blue: #0355a3;
    --mid-blue: #3176b5;
    --green: #9ccb3b;
    --lime: #acd037;
    --white: #ffffff;
    --ink: #1f3b72;
    --dot-grey: #b9b9b9;
    --stripe-a: #f3f3f3;
    --stripe-b: #e4e4e4;
    --icon-grey: #444444;
  }
  * { box-sizing: border-box; margin: 0; padding: 0; }
  html, body { width: 1200px; height: 2857px; overflow: hidden; }
  body {
    font-family: "Arimo", Arial, sans-serif;
    background: var(--white);
    position: relative;
  }
  .site-header { position: absolute; left: 0; top: 0; width: 1200px; height: 243px; background: var(--white); }
  .menu-toggle { position: absolute; left: 137px; top: 103px; width: 63px; height: 42px; }
  .brand-name {
    position: absolute; left: 250px; top: 98px;
    font-size: 46px; line-height: 52px; font-weight: 700; color: var(--brand-blue);
    white-space: nowrap;
  }
  .tagline {
    position: absolute; left: 600px; top: 70px; width: 450px; text-align: center;
    font-size: 46px; line-height: 50px; color: var(--green); letter-spacing: 0.5px;
  }
  .search-band { position: absolute; left: 0; top: 243px; width: 1200px; height: 171px; background: var(--brand-blue); }
  .search-form {
    position: absolute; left: 151px; top: 46px; width: 886px; height: 80px;
    background: var(--white); border-radius: 18px; overflow: hidden;
  }
  .search-input {
    position: absolute; left: 34px; top: 0; line-height: 80px;
    font-size: 40px; font-style: italic; color: #333;
  }
  .search-go {
    position: absolute; right: 0; top: 0; width: 203px; height: 80px; border-radius: 18px;
    background: var(--green); color: var(--white); font-size: 40px; font-weight: 700;
    text-align: center; line-height: 80px;
  }
  .striped {
    position: absolute; left: 0; width: 1200px;
    background: repeating-linear-gradient(135deg, var(--stripe-a) 0 8px, var(--stripe-b) 8px 12px);
  }
  .hero-area { top: 414px; height: 1600px; }
  .slider {
    position: absolute; left: 134px; top: 32px; width: 917px; height: 1531px;
    border: 6px solid var(--white);
    background: linear-gradient(180deg, #8ea8c9 0%, #a9b3b9 30%, #7d7a63 55%, #8b6d5a 100%);
  }
  .slide-caption {
    position: absolute; left: 0; right: 0; top: 1128px; height: 206px;
    background: rgba(40, 40, 40, 0.45);
    color: var(--white); font-size: 63px; text-align: center; line-height: 206px; letter-spacing: 1.5px;
    white-space: nowrap;
  }
  .intro { position: absolute; left: 0; top: 2014px; width: 1200px; height: 566px; background: var(--white); }
  .slider-dots { position: absolute; left: 480px; top: 40px; display: flex; gap: 14px; }
  .slider-dots span { width: 40px; height: 40px; border-radius: 50%; background: var(--mid-blue); }
  .slider-dots span.is-active { background: var(--dot-grey); }
  .intro-text {
    position: absolute; left: 137px; top: 172px; width: 1000px;
    font-size: 63px; line-height: 69px; color: var(--ink); letter-spacing: 1px;
  }
  .intro-text span { display: block; white-space: nowrap; }
  .footer-area { top: 2580px; height: 277px; }
  .site-footer {
    position: absolute; left: 137px; top: 37px; width: 914px; height: 240px;
    background: var(--brand-blue); color: var(--white);
  }
  .footer-nav { position: absolute; left: 0; top: 30px; width: 914px; height: 44px; font-size: 37px; font-weight: 700; }
  .footer-nav span { position: absolute; top: 0; line-height: 44px; white-space: nowrap; }
  .footer-nav .sep { font-weight: 400; font-style: italic; }
  .legal {
    position: absolute; left: 37px; top: 112px; font-size: 30px; line-height: 34px;
    font-weight: 700; letter-spacing: 0.8px; white-space: nowrap;
  }
</style>
</head>
<body>
  <header class="site-header">
    <svg class="menu-toggle" viewBox="0 0 63 42" aria-label="Menu">
      <rect x="0" y="0" width="63" height="8" fill="var(--icon-grey)"/>
      <rect x="0" y="17" width="63" height="8" fill="var(--icon-grey)"/>
      <rect x="0" y="34" width="63" height="8" fill="var(--icon-grey)"/>
    </svg>
    <div class="brand-name">RP Consult</div>
    <p class="tagline">“Working to Sustain<br>our Environments”</p>
  </header>

  <section class="search-band">
    <div class="search-form">
      <span class="search-input">Search...</span>
      <span class="search-go">Go</span>
    </div>
  </section>

  <section class="striped hero-area">
    <div class="slider" role="img" aria-label="Two field technicians in hard hats and hi-vis vests lowering a monitoring probe into a groundwater well">
      <div class="slide-caption">Groundwater Monitoring</div>
    </div>
  </section>

  <section class="intro">
    <div class="slider-dots">
      <span></span><span></span><span class="is-active"></span><span></span><span></span><span></span>
    </div>
    <p class="intro-text">
      <span>We are a company offering</span>
      <span>environmental services to</span>
      <span>clients in the private and</span>
      <span>goverment sectors throughout</span>
      <span>Australia</span>
    </p>
  </section>

  <section class="striped footer-area">
    <footer class="site-footer">
      <nav class="footer-nav">
        <span style="left:43px">Home</span>
        <span class="sep" style="left:190px">/</span>
        <span style="left:249px">About</span>
        <span class="sep" style="left:395px">/</span>
        <span style="left:457px">Services</span>
        <span class="sep" style="left:635px">/</span>
        <span style="left:686px">Contact</span>
      </nav>
      <p class="legal">
        Copyright&nbsp; 2014 - River &amp; Plains Consulting Pty Ltd<br>
        Also trading as RP Consult - All rights reserved<br>
        ABN 12 345 678 901
      </p>
    </footer>
  </section>
</body>
</html>
```